Medical Eye Care Practice needs a unique business card design.

I need a business card for my medical, eye care practice. I am seeking a unique design, possibly with a vertical or atypical shape layout -- something to make the card stand out. I would like the final design to communicate health and wellness with a contemporary feel. Please incorporate my logo and slogan with a color scheme based off of my logo. It should also identify all of the information that is listed on my sample business card. The back side should be utilized for appointment reminder with date, time, and room for notes. I would also like some incorporation of facebook, twitter, and google plus links.

```html
<!DOCTYPE html>
<html lang="en">
<head>
<meta charset="utf-8">
<title>Lakecrest Eye Care – Business Card</title>
<link rel="stylesheet" href="https://fonts.googleapis.com/css2?family=Questrial&display=swap">
<style>
  :root {
    --backdrop: #9a9a9a;
    --card-white: #f7f7f5;
    --leaf: #b9d27a;
    --leaf-soft: #c3d98c;
    --earth: #7f6647;
    --slate: #4f5a6b;
    --ink: #1f1f1f;
    --tan: #b08a5c;
  }
  * { box-sizing: border-box; margin: 0; padding: 0; }
  html, body { width: 1200px; height: 757px; overflow: hidden; }
  body {
    background: var(--backdrop);
    font-family: "Questrial", sans-serif;
    color: var(--ink);
    position: relative;
  }
  .card {
    position: absolute;
    top: 78px;
    width: 360px;
    height: 600px;
    box-shadow: 0 6px 18px rgba(0,0,0,.25);
  }

  /* Practice name */
  .practice { display: flex; align-items: center; justify-content: center; gap: 10px; }
  .practice__dot { width: 16px; height: 16px; border-radius: 50%; background: var(--earth); flex: none; }
  .practice__name { font-family: "Questrial", sans-serif; font-weight: 400; color: var(--earth); }
  .slogan { color: var(--slate); letter-spacing: .4px; }

  /* Contact side */
  .card--front {
    left: 190px;
    background: var(--card-white);
    border-top: 14px solid var(--leaf);
    border-bottom: 14px solid var(--leaf);
    text-align: center;
    padding: 40px 28px 0;
  }
  .card--front .practice__name { font-size: 26px; }
  .card--front .slogan { font-size: 11px; margin-top: 8px; }
  .person__name { font-size: 25px; font-weight: 400; margin-top: 20px; letter-spacing: .5px; }
  .person__title { font-size: 14px; color: var(--tan); letter-spacing: 1px; margin-top: 2px; }
  .contact { list-style: none; margin-top: 14px; }
  .contact li { display: flex; flex-direction: column; align-items: center; margin-bottom: 8px; font-size: 15px; line-height: 1.25; }
  .contact__icon {
    width: 20px; height: 20px; border-radius: 50%;
    background: var(--tan); margin-bottom: 4px;
    display: flex; align-items: center; justify-content: center;
  }
  .contact__icon svg { width: 12px; height: 12px; fill: #fff; }
  .appointment { text-align: left; font-size: 15px; margin-top: 10px; }
  .appointment p { display: flex; align-items: baseline; margin-bottom: 12px; }
  .appointment .dots { flex: 1; border-bottom: 2px dotted var(--ink); margin: 0 4px; height: 1px; }

  /* Brand side */
  .card--back { left: 650px; background: var(--leaf-soft); }
  .card--back .brand { position: absolute; top: 250px; left: 0; right: 0; text-align: center; }
  .card--back .practice__dot { width: 22px; height: 22px; }
  .card--back .practice__name { font-size: 36px; }
  .card--back .slogan { font-size: 14px; margin-top: 12px; }
  .web { font-size: 14px; color: var(--slate); margin-top: 4px; }
  .social { position: absolute; bottom: 22px; left: 0; right: 0; display: flex; justify-content: center; gap: 10px; }
  .social span { width: 26px; height: 26px; border-radius: 50%; background: var(--earth); }
</style>
</head>
<body>
  <section class="card card--front">
    <div class="practice">
      <span class="practice__dot"></span>
      <span class="practice__name">Lakecrest Eye Care</span>
    </div>
    <p class="slogan">Clear Sight • Good Health • Full Life</p>
    <h1 class="person__name">Dana Whitlow</h1>
    <p class="person__title">OD | FAAO</p>
    <ul class="contact">
      <li><span class="contact__icon"><svg viewBox="0 0 24 24"><path d="M6.6 10.8a15 15 0 0 0 6.6 6.6l2.2-2.2a1 1 0 0 1 1-.25 11 11 0 0 0 3.6.6 1 1 0 0 1 1 1V20a1 1 0 0 1-1 1A17 17 0 0 1 3 4a1 1 0 0 1 1-1h3.5a1 1 0 0 1 1 1 11 11 0 0 0 .6 3.6 1 1 0 0 1-.25 1z"/></svg></span>(555) 014-2210</li>
      <li><span class="contact__icon"><svg viewBox="0 0 24 24"><path d="M6 2h9v5H6zM4 8h16a2 2 0 0 1 2 2v8H2v-8a2 2 0 0 1 2-2zm3 12h10v2H7z"/></svg></span>(555) 014-2211</li>
      <li><span class="contact__icon"><svg viewBox="0 0 24 24"><path d="M4 3l16 7-7 2-2 7z"/></svg></span>www.lakecrest-eye.com</li>
      <li><span class="contact__icon"><svg viewBox="0 0 24 24"><path d="M12 2a7 7 0 0 0-7 7c0 5 7 13 7 13s7-8 7-13a7 7 0 0 0-7-7zm0 9.5A2.5 2.5 0 1 1 12 6.5a2.5 2.5 0 0 1 0 5z"/></svg></span>210 Harbor Rd. Suite 400<br>Brookfield, Wi 53000</li>
    </ul>
    <div class="appointment">
      <p>Date:<span class="dots"></span>Time:<span class="dots"></span></p>
      <p>Reason for Visit:<span class="dots"></span></p>
      <p><span class="dots"></span></p>
    </div>
  </section>

  <section class="card card--back">
    <div class="brand">
      <div class="practice">
        <span class="practice__dot"></span>
        <span class="practice__name">Lakecrest Eye Care</span>
      </div>
      <p class="slogan">Clear Sight • Good Health • Full Life</p>
      <p class="web">www.lakecrest-eye.com</p>
    </div>
    <div class="social" aria-label="Social media links">
      <span></span><span></span><span></span>
    </div>
  </section>
</body>
</html>
```